Redesign of an existing homepage

This site needs a redesign
https://www.ferien-am-haldbach.de
This page with the accommodation options is important for the customer
https://www.ferien-am-haldbach.de/gastgeber/
Till now there is a new logo. See attachment. That's all I have.
It would make sense to use the colors of the logo in the redesign.
footer.jpg.
I would put this info into the footer. The graphic (Infomaterial) is not needed.
a new menu - links.jpg
This info can be put in a new menu. Therefore the right column is gone and there is more space for the design.
NEW:
Please keep in mind that the Icons are important and shall be displayed under every accommodation
Number of Pages Required
1 page

```html
<!DOCTYPE html>
<html lang="de">
<head>
<meta charset="utf-8">
<title>Tourismusverband Haldbach – Urlaub im Haldtal</title>
<link href="https://fonts.googleapis.com/css2?family=Figtree:wght@400;600;700;800&family=Questrial&display=swap" rel="stylesheet">
<style>
:root{
  --brand-blue:#2aa3d9;
  --brand-blue-dark:#1f7fb6;
  --brand-navy:#1d5a9c;
  --brand-green:#7ab929;
  --header-bg:#f9f8f7;
  --nav-bg:#dcdcdc;
  --text-dark:#1c1c1c;
  --info-bg:#222530;
  --footer-bg:#100b0b;
  --placeholder:#d9dde2;
  --placeholder-dark:#b9c0c8;
  --white:#ffffff;
}
*{margin:0;padding:0;box-sizing:border-box}
html,body{width:1200px;height:2441px;overflow:hidden}
body{position:relative;background:var(--header-bg);font-family:"Questrial",sans-serif;color:var(--text-dark)}
.abs{position:absolute}

.site-header{left:0;top:0;width:1200px;height:205px;background:var(--header-bg)}
.brand{left:108px;top:40px;width:270px;text-align:center}
.brand-mark{display:inline-block;width:96px;height:96px;border-radius:50%;background:var(--brand-green)}
.brand-name{font-family:"Figtree",sans-serif;font-weight:800;font-size:25px;color:var(--brand-navy);line-height:1;margin-top:10px;letter-spacing:.2px}
.brand-sub{font-family:"Figtree",sans-serif;font-weight:800;font-size:25px;color:var(--brand-navy);line-height:1.1}
.top-link{top:149px;height:37px;background:var(--brand-blue);color:var(--white);font-family:"Figtree",sans-serif;font-size:26px;line-height:37px;text-align:center}

.main-nav{left:0;top:205px;width:1200px;height:51px;background:var(--nav-bg)}
.nav-item{top:0;height:51px;line-height:54px;font-family:"Figtree",sans-serif;font-weight:800;font-size:23px;color:var(--brand-blue)}
.nav-item.active{background:var(--brand-blue-dark);color:var(--white);text-align:center}

.hero{left:0;top:256px;width:1200px;height:676px;background:linear-gradient(180deg,#ecebe7 0%,#9a8c52 30%,#6b6a3a 55%,#a77a3c 80%,#c9a170 100%)}
.hero-caption{left:683px;top:586px;width:517px;height:171px;background:rgba(38,104,140,.72);color:var(--white);text-align:center}
.hero-title{font-family:"Figtree",sans-serif;font-weight:700;font-size:58px;line-height:1;margin-top:48px}
.hero-sub{font-family:"Figtree",sans-serif;font-size:28px;margin-top:4px}

.intro{left:0;top:932px;width:1200px;height:1296px;background:linear-gradient(180deg,#5f8cc4 0%,#8fb3d6 40%,#c7d6df 62%,#8fb23f 72%,#4f8a1c 100%)}
.intro-text{left:82px;top:986px;width:787px;font-size:22px;letter-spacing:.45px;line-height:31px;text-align:justify;color:var(--text-dark)}
.intro-text p{margin-bottom:31px}
.intro-text p.tight{margin-bottom:0}

.info-box{left:899px;top:932px;width:273px;height:441px;background:var(--info-bg);color:var(--white);padding:92px 0 0 27px;font-family:"Figtree",sans-serif;font-weight:600;font-size:14.5px;line-height:20.5px}
.info-box h2{font-weight:700;font-size:46px;line-height:1;color:var(--brand-blue);margin:0 0 2px -2px}
.info-box .gap{height:20px}

.guide-photo{left:815px;top:1531px;width:385px;height:697px;background:linear-gradient(180deg,rgba(120,70,50,0) 0%,rgba(176,52,52,.55) 40%,rgba(170,40,44,.8) 100%);border-radius:180px 180px 0 0}

.partners{left:0;top:1780px;width:163px;height:448px;background:var(--white)}
.badge{left:13px;width:128px;background:var(--placeholder);border-radius:4px}

.site-footer{left:0;top:2228px;width:1200px;height:213px;background:var(--footer-bg);color:#e8e8e8}
.footer-title{font-family:"Figtree",sans-serif;font-weight:600;font-size:23px;line-height:28px;color:var(--brand-blue)}
.footer-text{font-size:17px;line-height:24px}
.footer-btn{height:28px;background:var(--brand-blue);color:var(--white);font-size:17px;line-height:28px;padding-left:7px}
</style>
</head>
<body>

<header class="abs site-header">
  <div class="abs brand">
    <span class="brand-mark"></span>
    <div class="brand-name">TOURISMUSVERBAND</div>
    <div class="brand-sub">HALDBACH</div>
  </div>
  <a class="abs top-link" style="left:621px;width:162px">Infomaterial</a>
  <a class="abs top-link" style="left:807px;width:162px">Impressum</a>
  <a class="abs top-link" style="left:993px;width:163px">Datenschutz</a>
</header>

<nav class="abs main-nav">
  <span class="abs nav-item active" style="left:0;width:130px">HOME</span>
  <span class="abs nav-item" style="left:137px">GASTGEBER</span>
  <span class="abs nav-item" style="left:300px">HALDTAL</span>
  <span class="abs nav-item" style="left:426px">FREIZEIT</span>
  <span class="abs nav-item" style="left:551px">AUSFLUGSZIELE</span>
  <span class="abs nav-item" style="left:776px">KUNST UND KULTUR</span>
  <span class="abs nav-item" style="left:1052px">KONTAKT</span>
</nav>

<section class="abs hero" role="img" aria-label="Foto: junge Familie mit Kleinkind spaziert im Herbstlicht über eine Wiese vor Bäumen"></section>
<div class="abs hero-caption">
  <div class="hero-title">Urlaub im Haldtal</div>
  <div class="hero-sub">dem schönsten Fleck Bayerns</div>
</div>

<section class="abs intro" role="img" aria-label="Hintergrundfoto: blauer Himmel mit Wolken über einer grünen Wiese"></section>

<div class="abs intro-text">
  <p>Lieber Besucherinnen und Besucher,<br>Haldbach und Umgebung haben all das, was das Leben lebenswert macht:<br>Kultur und Natur, Lebensfreude und Genuss, freundliche und aufgeschlossene Menschen...</p>
  <p>Ob Kirchen, Brunnen oder andere Baudenkmäler - bei einem Rundgang durch die Haldtaler Ross-Stadt kann man viele liebevolle Details für sich entdecken.</p>
  <p>Für Bewegungsfreudige und Erholungssuchende gibt es "Natur pur" in und um Haldbach! Hier kann man sportlich unterwegs sein beim Radeln, Walken, Wandern, Golfen, Reiten und Baden oder einfach nur die Ruhe genießen.</p>
  <p>Freizeit und Erholung für die ganze Familie - planen Sie einen Urlaub auf dem Bauernhof, in einer Ferienwohnung oder im Hotel. Ihr Urlaub im Haldtal wird ein einmaliges Erlebnis!</p>
  <p>Genießen Sie unsere Gastfreundschaft - ein Besuch lohnt sich zu jeder Jahreszeit.<br>Wir freuen uns auf Sie!<br>Ihr</p>
  <p class="tight">Fremdenverkehrsverein Haldbach und Umgebung e. V.</p>
</div>

<aside class="abs info-box">
  <h2>FVV HLB</h2>
  Fremdenverkehrsverein<br>Haldbach und Umgebung e. V.<br>Marktplatz 4<br>84390 Haldbach
  <div class="gap"></div>
  Tel.: 08570 / 412 2230<br>Fax: 08570 / 412 2239<br>tourist-info@haldbach-ferien.de
  <div class="gap"></div>
  Öffnungszeiten:<br>Mo-Fr 9:00 - 17:00 Uhr<br>Mai-Oktober:<br>Sa 9:00-12:00 Uhr
</aside>

<div class="abs guide-photo" role="img" aria-label="Foto: junge Frau im rot-weiß gestreiften Pullover zeigt begeistert auf den Text"></div>

<div class="abs partners" role="img" aria-label="Partnerzeichen">
  <div class="abs badge" style="top:31px;height:88px"></div>
  <div class="abs badge" style="top:140px;height:124px"></div>
  <div class="abs badge" style="top:288px;height:80px"></div>
  <div class="abs badge" style="top:381px;height:58px"></div>
</div>

<footer class="abs site-footer">
  <div class="abs" style="left:28px;top:22px">
    <div class="footer-title">Fremdenverkehrsverein<br>Haldbach und Umgebung e. V.</div>
    <div class="footer-text" style="margin-top:6px">Marktplatz 4<br>84390 Haldbach</div>
  </div>
  <div class="abs" style="left:429px;top:26px">
    <div class="footer-title">Kontakt</div>
    <div class="footer-text" style="margin-top:16px">Tel.: 08570 / 412 2230<br>Fax: 08570 / 412 2239</div>
    <div class="footer-btn" style="margin-top:16px;width:252px">tourist-info@haldbach-ferien.de</div>
  </div>
  <div class="abs" style="left:706px;top:28px">
    <div class="footer-title">Öffnungszeiten</div>
    <div class="footer-text" style="margin-top:14px">Mo-Do 9:00 - 16:00 Uhr<br>Fr&nbsp;&nbsp;&nbsp;&nbsp;&nbsp;&nbsp;&nbsp;&nbsp;&nbsp;&nbsp;9:00 - 12:30 Uhr</div>
  </div>
  <div class="abs" style="left:972px;top:28px">
    <div class="footer-title">Quicklinks</div>
    <div class="footer-btn" style="margin-top:12px;width:206px">Veranstaltungskalender</div>
    <div class="footer-btn" style="margin-top:19px;width:206px">Infomaterial</div>
  </div>
</footer>

</body>
</html>
```